Online Assistant Business needs sleek business card design

I need a contemporary / professional business card using the logo I have uploaded. I like simple clean designs. The business is an online (virtual) assistant business and my business card will be used at networking events and letter box dropped at local small to medium businesses.

Target Market(s)

Small to medium businesses

Industry/Entity Type

Consulting

Contact Information for Business Card

Corinne Wheatley
corinne@velqorahub.net.au
+ 61 (0) 491 570 156
www.velqorahub.net.au

```html
<!DOCTYPE html>
<html lang="en">
<head>
<meta charset="UTF-8">
<title>Velqora Hub – Business Card</title>
<link rel="stylesheet" href="https://fonts.googleapis.com/css2?family=Questrial&family=Didact+Gothic&display=swap">
<style>
  :root {
    --stage: #000000;
    --paper: #ffffff;
    --brand-blue: #2a95d4;
    --faint-blue: #5fa5d9;
    --ink-light: #ffffff;
  }
  * { margin: 0; padding: 0; box-sizing: border-box; }
  html, body {
    width: 1200px;
    height: 1200px;
    overflow: hidden;
    background: var(--stage);
  }
  .canvas {
    position: relative;
    width: 1200px;
    height: 1200px;
    background: var(--stage);
  }
  .card {
    position: absolute;
    left: 247px;
    width: 717px;
    height: 464px;
    overflow: hidden;
  }
  .card--front {
    top: 108px;
    background: var(--paper);
    display: flex;
    flex-direction: column;
    align-items: center;
    justify-content: center;
  }
  .brand-dot {
    width: 96px;
    height: 96px;
    border-radius: 50%;
    background: var(--brand-blue);
    margin-bottom: 22px;
    margin-top: -8px;
  }
  .brand-name {
    font-family: "Questrial", sans-serif;
    font-size: 70px;
    line-height: 1;
    letter-spacing: -1px;
    color: var(--brand-blue);
  }
  .card--back {
    top: 612px;
    background: var(--brand-blue);
  }
  .back-circle {
    position: absolute;
    left: 36px;
    top: -82px;
    width: 352px;
    height: 352px;
    border-radius: 50%;
    background: var(--faint-blue);
  }
  .contact {
    position: absolute;
    right: 60px;
    top: 234px;
    text-align: right;
    color: var(--ink-light);
  }
  .contact__name {
    font-family: "Questrial", sans-serif;
    font-size: 37px;
    font-weight: 400;
    letter-spacing: 0.5px;
    -webkit-text-stroke: 0.6px var(--ink-light);
    line-height: 1;
    margin-bottom: 36px;
  }
  .contact__line {
    font-family: "Didact Gothic", sans-serif;
    font-size: 29px;
    line-height: 35px;
    letter-spacing: 0.6px;
  }
</style>
</head>
<body>
  <main class="canvas">
    <section class="card card--front" aria-label="Card front">
      <div class="brand-dot"></div>
      <p class="brand-name">velqora hub</p>
    </section>

    <section class="card card--back" aria-label="Card back">
      <div class="back-circle"></div>
      <div class="contact">
        <h1 class="contact__name">Corinne Wheatley</h1>
        <p class="contact__line">corinne@velqorahub.net.au</p>
        <p class="contact__line">+ 61 (0) 491 570 156</p>
        <p class="contact__line">www.velqorahub.net.au</p>
      </div>
    </section>
  </main>
</body>
</html>
```